Stationery Set for new venture capital firm

We need a new set of stationery including letterhead, business cards, envelopes, with compliment slips for our new startup venture capital firm known as Halvora.
We make alternative investments globally and hope to have a worldwide network of offices later.

The stationery should be elegant and not too fussy with the use of too many colors.

Venture Capital

```html
<!DOCTYPE html>
<html lang="en">
<head>
<meta charset="utf-8">
<title>Halvora Stationery</title>
<link href="https://fonts.googleapis.com/css2?family=Open+Sans:wght@400;600;700&display=swap" rel="stylesheet">
<style>
  :root {
    --bg: #eceef0;
    --paper: #ffffff;
    --ink: #1e1e1e;
    --grey: #8b8d90;
    --faint: #f1f1f2;
    --blue: #1b8fcf;
  }
  * { box-sizing: border-box; margin: 0; padding: 0; }
  html, body { width: 1200px; height: 800px; overflow: hidden; }
  body {
    background: var(--bg);
    font-family: "Open Sans", Arial, sans-serif;
    color: var(--ink);
    position: relative;
  }
  .letterhead {
    position: absolute; left: 70px; top: 60px;
    width: 480px; height: 680px;
    background: var(--paper);
    box-shadow: 0 6px 18px rgba(0,0,0,0.08);
    overflow: hidden;
    padding: 48px 50px;
  }
  .letterhead .backdrop {
    position: absolute; right: -120px; top: 60px;
    width: 380px; height: 380px; border-radius: 50%;
    background: var(--faint);
  }
  .brand { display: flex; align-items: center; gap: 8px; position: relative; }
  .brand .dot { width: 14px; height: 14px; border-radius: 50%; background: var(--blue); }
  .brand .name { font-weight: 700; color: var(--grey); }
  .letterhead .brand { justify-content: center; }
  .letterhead .brand .name { font-size: 30px; }
  .letter { position: relative; font-size: 9px; line-height: 1.45; margin-top: 60px; }
  .letter .date { font-weight: 700; margin-bottom: 14px; }
  .letter .recipient { margin-bottom: 14px; }
  .letter .salutation { font-weight: 700; margin-bottom: 12px; }
  .letter p { margin-bottom: 10px; }
  .closing { position: relative; margin-top: 26px; font-size: 9px; line-height: 1.45; }
  .closing .signer { margin-top: 36px; font-weight: 600; }
  .letter-footer {
    position: absolute; right: 50px; bottom: 44px;
    font-size: 8.5px; line-height: 1.5; color: #555; text-align: left;
  }
  .letter-footer .gap { height: 8px; }

  .card {
    position: absolute; width: 360px; height: 210px;
    box-shadow: 0 6px 16px rgba(0,0,0,0.12);
    overflow: hidden;
  }
  .card-back { left: 640px; top: 150px; background: var(--blue); color: #fff; }
  .card-back .backdrop {
    position: absolute; left: 150px; top: -40px;
    width: 260px; height: 260px; border-radius: 50%;
    background: rgba(255,255,255,0.9);
  }
  .card-back .contact { position: absolute; left: 24px; bottom: 24px; font-size: 10.5px; line-height: 1.5; }
  .card-back .web { margin-top: 8px; }
  .card-front { left: 640px; top: 430px; background: var(--paper); }
  .card-front .backdrop {
    position: absolute; left: 110px; top: 20px;
    width: 220px; height: 220px; border-radius: 50%;
    background: #e3e3e4;
  }
  .card-front .brand { position: absolute; left: 20px; top: 22px; }
  .card-front .brand .name { font-size: 16px; }
  .card-front .person { position: absolute; left: 140px; top: 64px; text-align: center; width: 170px; }
  .card-front .person-name { font-size: 19px; }
  .card-front .person-role { font-size: 19px; color: var(--blue); }
  .card-front .address { position: absolute; left: 20px; bottom: 20px; font-size: 11px; line-height: 1.5; }
</style>
</head>
<body>
  <section class="letterhead">
    <div class="backdrop"></div>
    <div class="brand"><span class="dot"></span><span class="name">Halvora</span></div>
    <div class="letter">
      <div class="date">March 30, 2014</div>
      <div class="recipient">Northfield Partners<br>12th Floor, Meridian Tower<br>88 Alder Street<br>Portland, OR 97205</div>
      <div class="salutation">Dear Mr. Okafor,</div>
      <p>Morbi mollis leo, et tristique nisi pharetra vel. Proin ultrices, nunc rutrum dictum, felis ligula interdum nulla, blandit egestas lorem orci vehicula lacus. Vivamus tempor quam molestie nisi egestas volutpat. Sed eget purus ante.</p>
      <p>Phasellus vel ligula ac magna varius vestibulum pellentesque at ipsum porta, dapibus ipsum quis, malesuada purus. Mauris tortor eget faucibus. Praesent aliquet ante in odio tristique lorem feugiat. Nam id lectus sem.</p>
      <p>Aenean egestas. Phasellus dui odio, lacinia nec arcu pharetra tellus. Fusce et lorem nisi. Vivamus orci elementum eget. Sed et tortor id pharetra ut ipsum ac egestas.</p>
    </div>
    <div class="closing">
      <div>Yours sincerely,</div>
      <div class="signer">PETRA LINDQVIST<br>Manager</div>
    </div>
    <address class="letter-footer" style="font-style:normal">
      Halvora<br>
      18th Floor, Quayside Exchange<br>
      7 Pier Lane, Eastbourne Bay
      <div class="gap"></div>
      Tel +44 20 7946 0321<br>
      Fax +44 20 7946 0322<br>
      www.halvoracapital.example
    </address>
  </section>

  <section class="card card-back">
    <div class="backdrop"></div>
    <div class="contact">
      Tel +44 20 7946 0321<br>
      Fax +44 20 7946 0322
      <div class="web">www.halvoracapital.example</div>
    </div>
  </section>

  <section class="card card-front">
    <div class="backdrop"></div>
    <div class="brand"><span class="dot"></span><span class="name">Halvora</span></div>
    <div class="person">
      <div class="person-name">Elias Marlow</div>
      <div class="person-role">CEO</div>
    </div>
    <div class="address">18th Floor, Quayside Exchange<br>7 Pier Lane, Eastbourne Bay</div>
  </section>
</body>
</html>
```